PINE HOLLOW BUILDERS leave behind sales FLYER 8.5"x11"

We need a high quality advertising flyer 8.5"x11" for our construction company offering kitchen and bathroom remodels. Can be front and back or just the front of the flyer depending on the design. phone number to come
www.brightmortarworks.example

we are also a home inspection company. We will leave this at the home when we are done with our home inspections for our new home owners

Target Market(s)

Home owners

Industry/Entity Type

Residential Construction

Contact Information for Business Card

We want it to match the flyer please

Requirements
Must have
• My logo, my website , my phone number (to come later),
• FL State Lic. #CRC8047163 & Insured
• We Specialize in Bathroom and Kitchen remodeling ,new Construction & Interior or Exterior home Renovations, garages and more! Serving Central Florida for over 15 years.
• Family owned and operated,
• we perform all levels of building and remodeling.
• i wouldn't mind seeing what you come up with for text on the flyer.
Nice to have
• maybe a nice kitchen and bathroom pictures

```html
<!DOCTYPE html>
<html lang="en">
<head>
<meta charset="utf-8">
<title>Pine Hollow Builders – Kitchen and Bathroom Remodeling Flyer</title>
<link rel="stylesheet" href="https://fonts.googleapis.com/css2?family=Cinzel:wght@600&family=Open+Sans:ital,wght@0,400;0,600;0,700;1,700&display=swap">
<style>
  :root {
    --wood-dark: #5a3420;
    --wood-mid: #744630;
    --wood-light: #84553a;
    --rule: #c9ab80;
    --cream: #e9dfc4;
    --text: #f6efe4;
    --white: #ffffff;
    --logo-panel: #e6e4e1;
    --logo-ink: #5b5b5b;
  }
  * { margin: 0; padding: 0; box-sizing: border-box; }
  html, body { width: 927px; height: 1200px; overflow: hidden; }
  body { font-family: "Open Sans", Arial, sans-serif; color: var(--text); }

  .flyer {
    position: relative;
    width: 927px;
    height: 1200px;
    overflow: hidden;
    background:
      repeating-linear-gradient(90deg, rgba(0,0,0,0.05) 0 3px, transparent 3px 11px, rgba(255,255,255,0.03) 11px 14px, transparent 14px 23px),
      linear-gradient(180deg, var(--wood-mid) 0%, var(--wood-light) 35%, var(--wood-mid) 65%, var(--wood-dark) 100%);
  }

  .grid { position: absolute; inset: 0; }

  .tagline {
    position: absolute; top: 26px; left: 0; width: 100%;
    text-align: center; font-style: italic; font-weight: 700;
    font-size: 38px; line-height: 50px; color: var(--cream);
  }
  .headline {
    position: absolute; top: 88px; left: 0; width: 100%;
    text-align: center; font-family: "Cinzel", Georgia, serif;
    font-weight: 600; font-size: 35px; line-height: 44px; color: var(--cream); letter-spacing: 0.3px;
  }

  .section-title { font-weight: 700; font-size: 15.5px; color: var(--white); text-transform: uppercase; margin-bottom: 8px; }
  .body-copy { font-size: 14.4px; line-height: 20px; }
  .body-copy + .body-copy { margin-top: 8px; }

  .about { position: absolute; top: 168px; left: 70px; width: 310px; }
  .services { position: absolute; top: 337px; left: 70px; width: 312px; }
  .service-list { list-style: none; margin-top: 10px; }
  .service-list li { font-size: 14.4px; line-height: 20px; padding-left: 16px; position: relative; }
  .service-list li::before {
    content: ""; position: absolute; left: 1px; top: 7px;
    width: 6px; height: 6px; border-radius: 50%; background: var(--text);
  }

  .kitchen-photo {
    position: absolute; left: 418px; top: 168px; width: 460px; height: 638px;
    background: linear-gradient(180deg, #f3f2ee 0%, #e9e6df 45%, #d8d3c8 62%, #8a5c38 78%, #6e4526 100%);
  }

  .design-kicker { position: absolute; top: 790px; left: 118px; font-weight: 700; font-size: 15px; color: var(--white); }
  .design-word { position: absolute; top: 812px; left: 118px; font-weight: 600; font-size: 33px; color: var(--white); letter-spacing: 0.8px; }

  .bath-stamp {
    position: absolute; left: 67px; top: 878px; width: 318px; height: 258px;
    background: var(--white); padding: 16px;
  }
  .bath-photo {
    width: 100%; height: 100%;
    background: linear-gradient(160deg, #b79a6a 0%, #8f6a3e 40%, #5c3c22 70%, #c8b79c 100%);
  }

  .inspection { position: absolute; top: 823px; left: 416px; width: 460px; }
  .inspection .section-title { font-size: 20px; text-align: center; margin-bottom: 5px; }
  .inspection .body-copy { font-size: 13.3px; line-height: 20px; }

  .contact {
    position: absolute; top: 1018px; left: 406px; width: 222px;
    font-style: normal; font-size: 14.4px; line-height: 21.5px;
  }
  .contact .license { font-size: 12px; font-weight: 600; color: var(--cream); }
  .contact .web { font-weight: 700; font-size: 12.4px; white-space: nowrap; }
  .contact svg { vertical-align: -2px; margin-right: 3px; }

  .logo-panel {
    position: absolute; left: 636px; top: 985px; width: 261px; height: 166px;
    background: var(--logo-panel);
    display: flex; flex-direction: column; align-items: center; justify-content: center; gap: 10px;
  }
  .logo-mark { width: 14px; height: 14px; background: var(--logo-ink); }
  .logo-name { font-weight: 700; font-size: 20px; color: var(--logo-ink); text-align: center; letter-spacing: 1px; line-height: 26px; }
</style>
</head>
<body>
<main class="flyer">
  <svg class="grid" width="927" height="1200" viewBox="0 0 927 1200" aria-hidden="true">
    <g stroke="var(--rule)" stroke-width="1.5" fill="none">
      <line x1="0" y1="155" x2="927" y2="155"/>
      <line x1="0" y1="323" x2="398" y2="323"/>
      <line x1="0" y1="815" x2="927" y2="815"/>
      <line x1="0" y1="1158" x2="927" y2="1158"/>
      <line x1="47" y1="155" x2="47" y2="1200"/>
      <line x1="398" y1="155" x2="398" y2="815"/>
      <line x1="897" y1="155" x2="897" y2="1200"/>
      <line x1="634" y1="985" x2="634" y2="1158"/>
    </g>
    <g fill="var(--cream)" stroke="var(--wood-dark)" stroke-width="1.5">
      <circle cx="47" cy="155" r="9"/><circle cx="398" cy="155" r="9"/><circle cx="897" cy="155" r="9"/>
      <circle cx="47" cy="323" r="9"/><circle cx="398" cy="323" r="9"/>
      <circle cx="47" cy="815" r="9"/><circle cx="398" cy="815" r="9"/><circle cx="897" cy="815" r="9"/>
      <circle cx="634" cy="985" r="9"/><circle cx="897" cy="985" r="9"/>
      <circle cx="47" cy="1158" r="9"/><circle cx="634" cy="1158" r="9"/><circle cx="897" cy="1158" r="9"/>
    </g>
  </svg>

  <p class="tagline">Time for an update?</p>
  <h1 class="headline">KITCHEN AND BATHROOM REMODELING</h1>

  <section class="about">
    <h2 class="section-title">About Us</h2>
    <p class="body-copy">We Specialize in New Construction &amp; Interior or Exterior home Renovations, Including Bathroom and kitchen remodeling, garages and more! Serving Ocala/Marion county for over 10 years.</p>
  </section>

  <section class="services">
    <h2 class="section-title">Our Services</h2>
    <p class="body-copy">Family owned and operated, we perform all levels of building and remodeling. We offer start-to-finish solutions for every project. We specialize in interior or exterior home renovations, including bathroom and kitchen remodeling, home additions, garages and more!</p>
    <p class="body-copy">We guarantee high-quality construction for each and every project. Check out samples of our recent work,and you'll agree that we're the best choice for your home renovation project.</p>
    <ul class="service-list">
      <li>NEW CONSTRUCTION</li>
      <li>BARNS</li>
      <li>REMODELS</li>
      <li>RENOVATIONS</li>
      <li>REPAIRS</li>
      <li>KITCHENS</li>
      <li>BATHROOMS</li>
      <li>BANK REMODELS</li>
    </ul>
  </section>

  <div class="kitchen-photo" role="img" aria-label="Photo of a bright white remodeled kitchen with coffered ceiling, island and wood floor"></div>

  <p class="design-kicker">We design for</p>
  <p class="design-word">Functionality</p>

  <div class="bath-stamp">
    <div class="bath-photo" role="img" aria-label="Photo of a remodeled bathroom with soaking tub, glass block window and vanity"></div>
  </div>

  <section class="inspection">
    <h2 class="section-title">Home Inspection Service</h2>
    <p class="body-copy">Not only do we specialize in renovations and remodeling, but also home inpections. Get the best in a quality home inspection report to help you make the best decision of the price being asked. We strongly encourage you to attend the inspection providing you with the opportunity to ask questions about the systems and components of the property and enabling you to receive first-hand answers, on site.</p>
  </section>

  <address class="contact">
    <span class="license">FL State Lic. #CRC8047163 &amp; Insured</span><br>
    418 Cypress Bend Rd.<br>
    Marlow, FL 34999, USA<br>
    <svg width="13" height="13" viewBox="0 0 24 24" aria-hidden="true"><circle cx="12" cy="12" r="11" fill="none" stroke="var(--text)" stroke-width="2"/><path d="M8 6c-1 1-1 3 1 6s4 5 6 5c1 0 2-1 2-2l-2-2-2 1c-1-1-3-3-3-4l1-2-2-2z" fill="var(--text)"/></svg>555.014.2286<br>
    <span class="web">www.brightmortarworks.example</span>
  </address>

  <div class="logo-panel">
    <span class="logo-mark" aria-hidden="true"></span>
    <p class="logo-name">PINE HOLLOW<br>BUILDERS</p>
  </div>
</main>
</body>
</html>
```